Marlowe Grid Systems - Sales Brochure

I've been using the same sales Brochure for the past 10 years. I'm bored with it and I think my customers are bored with it. I'll be doing a lot of recruiting in 2014 for new vendors. I need something that pops out at them, flows with our website (www.getmarlowe-example.com) and says, I want to work with this cool company..

Target Market(s)

My target market is Computer / IT Consulting firms, Phone System Vendors.

Industry/Entity Type

It Company

Requirements
Must have
• Keep the language, product, carrier and service descriptions

```html
<!DOCTYPE html>
<html lang="en">
<head>
<meta charset="utf-8">
<title>Marlowe Grid Systems – Process Support</title>
<link rel="stylesheet" href="https://fonts.googleapis.com/css2?family=Open+Sans:wght@700&family=PT+Sans:wght@400&display=swap">
<style>
  :root {
    --ink: #4a4a4a;
    --title: #3c3f8c;
    --accent: #dd5424;
    --rule: #9a9a9a;
    --header-deep: #123f8c;
    --header-mid: #2f78c4;
    --header-glow: #d9f2ff;
    --paper-top: #ffffff;
    --paper-bottom: #f1f1f3;
  }
  * { margin: 0; padding: 0; box-sizing: border-box; }
  html, body { width: 958px; height: 1200px; overflow: hidden; }
  body {
    background: linear-gradient(to bottom, var(--paper-top) 55%, var(--paper-bottom));
    font-family: "PT Sans", "Myriad Pro", Arial, sans-serif;
    color: var(--ink);
    position: relative;
  }
  .hero { position: absolute; left: 0; top: 0; width: 958px; height: 430px; }
  .hero svg { display: block; }
  .hero-headline {
    position: absolute; right: 36px; top: 92px;
    text-align: right;
    font-family: "Open Sans", Arial, sans-serif;
    font-weight: 700; font-size: 42px; line-height: 54px;
    color: #fff; letter-spacing: 0.5px;
    text-shadow: 0 0 2px #0d2a5e, 1px 1px 2px #0d2a5e, -1px -1px 1px #0d2a5e;
  }
  .content { position: absolute; left: 32px; top: 398px; width: 900px; }
  .section-title { font-size: 42px; font-weight: 400; color: var(--title); line-height: 1.1; margin-bottom: 10px; }
  .topic h2 { font-size: 19px; font-weight: 400; color: var(--accent); line-height: 24px; }
  .topic p { font-size: 15.6px; line-height: 21.5px; margin-top: 3px; }
  .topic { margin-bottom: 14px; }
  .fit-list { list-style: none; margin-top: 6px; }
  .fit-list li {
    position: relative; padding-left: 16px;
    font-size: 15.6px; line-height: 22px; margin-bottom: 11.5px; max-width: 480px;
  }
  .fit-list li::before {
    content: ""; position: absolute; left: 1px; top: 8px;
    width: 6px; height: 6px; border-radius: 50%; background: var(--accent);
  }
  .footer-rule { position: absolute; left: 16px; right: 16px; top: 1087px; border-top: 1px solid var(--rule); }
  .brand {
    position: absolute; left: 42px; top: 1122px;
    display: flex; align-items: center; gap: 12px;
    font-size: 26px; color: var(--title);
  }
  .brand-dot { width: 18px; height: 18px; border-radius: 50%; background: var(--title); }
  .contact { position: absolute; right: 26px; top: 1100px; text-align: right; }
  .contact-label { font-size: 26px; color: var(--accent); line-height: 32px; }
  .contact-phone { font-size: 31px; color: var(--title); line-height: 36px; }
</style>
</head>
<body>
  <header class="hero">
    <svg width="958" height="430" viewBox="0 0 958 430" role="img" aria-label="Glowing blue stream of binary digits rushing toward a bright light burst">
      <defs>
        <radialGradient id="heroGlow" cx="0.48" cy="0.35" r="0.7">
          <stop offset="0" stop-color="var(--header-glow)"/>
          <stop offset="0.3" stop-color="#7cc3ef"/>
          <stop offset="0.65" stop-color="var(--header-mid)"/>
          <stop offset="1" stop-color="var(--header-deep)"/>
        </radialGradient>
        <linearGradient id="waveShade" x1="0" y1="0" x2="0" y2="1">
          <stop offset="0" stop-color="#d8d8dc"/>
          <stop offset="1" stop-color="#ffffff"/>
        </linearGradient>
      </defs>
      <rect width="958" height="430" fill="url(#heroGlow)"/>
      <path d="M0 372 C90 340 180 330 270 342 C450 365 640 430 800 422 C870 418 920 400 958 377 L958 430 L0 430 Z" fill="url(#waveShade)"/>
      <path d="M0 380 C90 350 180 342 270 352 C450 375 640 440 800 432 C870 428 920 410 958 387 L958 430 L0 430 Z" fill="#ffffff"/>
    </svg>
    <div class="hero-headline">PROVIDING<br>OUR PARTNERS<br>THE BEST IN<br>COMMUNICATION<br>SOLUTIONS</div>
  </header>

  <main class="content">
    <h1 class="section-title">Process Support</h1>

    <section class="topic">
      <h2>Product Selection and Pricing</h2>
      <p>Analyze the customer’s wants vs. what they really need and provide up to 3 cmpetitive quotes for telecom services.</p>
    </section>

    <section class="topic">
      <h2>Ordering Product</h2>
      <p>Deliver contract to the customer, review the agreement between the customer and the provider, submit the order, follow the progression of the order, make sure the proper people are on site for installation or porting of services, and follow up with the customer on completion of order.</p>
    </section>

    <section class="topic">
      <h2>Product Support</h2>
      <p>Customer is provided with an escalation sheet in case of any traumatic telecom occurrences.&nbsp; This sheet will outline the proper people to contact in the event of downtime.</p>
    </section>

    <section class="topic">
      <h2>A Good Customer for Marlowe Grid Systems:</h2>
      <p>Business that is:</p>
      <ul class="fit-list">
        <li>Unhappy with their current Telecom Service Provider</li>
        <li>Looking for business disaster recovery planning</li>
        <li>Upgrade the security, speed and optimization of their WAN</li>
        <li>Reduce their telecom monthly expenses</li>
        <li>Looking for Collocation facility</li>
        <li>Telecom Billing Optimization</li>
        <li>Interested in VOIP / SIP Trunking</li>
        <li>Needs a technology professional to work for their agenda, not the providers agenda.</li>
      </ul>
    </section>
  </main>

  <div class="footer-rule"></div>
  <div class="brand"><span class="brand-dot"></span><span class="brand-name">Marlowe Grid Systems</span></div>
  <div class="contact">
    <div class="contact-label">Call us on</div>
    <div class="contact-phone">555 010 4821</div>
  </div>
</body>
</html>
```